Sales Brochure- Generic Line Card 215mm x 140mm

Design a double-sided brochure similar to the attached sample. Cover Page contains a logo and theme that never changes. However, the background picture and the description text on the lower corner will be changed to advertise multiple services. Reverse-side contains Detailed Descriptive text related to the picture on Cover Page as well as Logo and Contact information for the business. Use the Kelvra Controls website www.kelvracontrols.ca for theme, color and contact information. Also, use attached business card design for theme to match. Use the supplied logo. SIZE 215mm x 140mm

Font styles to use
Sans Serif

Colors

Designer to choose colors to be used in the design.

Requirements
Must have
• Look Similar to Sample Brochure but include Kelvra Controls theme and colors

```html
<!DOCTYPE html>
<html lang="en">
<head>
<meta charset="utf-8">
<title>Kelvra Controls – Machining Line Card</title>
<link href="https://fonts.googleapis.com/css2?family=Montserrat:wght@300;400;500;600;700;800&display=swap" rel="stylesheet">
<style>
  :root {
    --page-bg: #8a8a8a;
    --orange: #f15a24;
    --orange-deep: #e0481a;
    --teal: #1a8f8f;
    --teal-dark: #0f5f63;
    --ink: #111315;
    --ink-soft: #1d2125;
    --white: #ffffff;
    --text-soft: #d9dcdf;
  }
  * { box-sizing: border-box; margin: 0; padding: 0; }
  html, body { width: 1200px; height: 2400px; overflow: hidden; }
  body {
    background: var(--page-bg);
    font-family: "Montserrat", Arial, sans-serif;
    position: relative;
  }
  .card {
    position: absolute;
    left: 50px;
    width: 1100px;
    height: 716px;
    overflow: hidden;
    box-shadow: 0 6px 18px rgba(0,0,0,.35);
  }
  .card--front { top: 424px; background: var(--ink); }
  .card--back { top: 1260px; background: var(--ink); }

  /* Front */
  .cover-photo {
    position: absolute; inset: 0;
    background: linear-gradient(112deg, #f77a2a 0%, var(--orange) 30%, var(--orange-deep) 40%, var(--teal) 47%, #137a7c 70%, var(--teal-dark) 100%);
  }
  .brand-tab {
    position: absolute; left: 0; top: 34px;
    width: 480px; height: 142px;
    background: var(--white);
    border-radius: 0 71px 71px 0;
    display: flex; align-items: center; gap: 18px;
    padding-left: 44px;
  }
  .brand-tab__mark { width: 32px; height: 32px; background: var(--teal); flex: none; }
  .brand-tab__name {
    font-weight: 800; font-size: 35px; color: var(--ink);
    letter-spacing: .3px; white-space: nowrap;
  }
  .tagline {
    position: absolute; left: 76px; top: 485px;
    border-left: 3px solid var(--white);
    padding-left: 14px;
    color: var(--white);
    font-size: 40px; line-height: 54px; font-weight: 300;
    letter-spacing: .5px;
  }
  .tagline strong { font-weight: 700; }
  .service-label {
    position: absolute; right: 0; top: 579px;
    display: flex; height: 64px;
  }
  .service-label__text {
    background: var(--white); color: var(--teal);
    border-radius: 14px 0 0 14px;
    width: 327px;
    display: flex; align-items: center; justify-content: center;
    font-size: 34px; font-weight: 500; letter-spacing: .5px;
  }
  .service-label__bar { width: 20px; background: var(--orange); }

  /* Back */
  .back-photo {
    position: absolute; inset: 0;
    background: radial-gradient(ellipse at 55% 45%, #2b3034 0%, var(--ink-soft) 45%, var(--ink) 100%);
  }
  .heading {
    position: absolute; left: 64px; top: 44px;
    border-left: 3px solid var(--orange);
    padding-left: 14px;
    color: var(--orange);
    font-size: 38px; line-height: 48px; font-weight: 400;
    letter-spacing: .5px;
  }
  .intro {
    position: absolute; left: 520px; top: 36px; width: 480px;
    color: var(--white); font-size: 17px; line-height: 26px; font-weight: 400;
  }
  .capabilities {
    position: absolute; top: 250px; list-style: none;
    color: var(--text-soft); font-size: 17px; font-weight: 500;
  }
  .capabilities--left { left: 62px; }
  .capabilities--right { left: 580px; }
  .capabilities li {
    display: flex; align-items: center; gap: 16px; height: 43px;
  }
  .capabilities svg { width: 20px; height: 20px; flex: none; }
  .info-band {
    position: absolute; left: 0; right: 0; top: 522px; height: 156px;
    background: var(--teal);
    border-top: 4px solid var(--white);
  }
  .highlights { position: absolute; left: 60px; top: 16px; list-style: none; }
  .highlights li {
    display: flex; align-items: center; gap: 16px; height: 41px;
    color: var(--white); font-size: 15px; font-weight: 700; letter-spacing: .3px;
  }
  .highlights svg { width: 22px; height: 22px; flex: none; }
  .gallery {
    position: absolute; left: 485px; top: 12px;
    display: flex; gap: 10px;
  }
  .gallery__item { width: 135px; }
  .gallery__photo {
    height: 100px;
    background: linear-gradient(135deg, #d9dcdc 0%, #8b9296 45%, #3c4246 100%);
  }
  .gallery__label {
    height: 24px; background: var(--ink);
    color: var(--orange); font-size: 11px; font-weight: 700;
    display: flex; align-items: center; justify-content: center;
    letter-spacing: .3px;
  }
  .contact-strip {
    position: absolute; left: 0; right: 0; bottom: 0; height: 38px;
    display: flex; align-items: center; justify-content: space-between;
    padding: 0 60px;
    color: var(--white); font-size: 13px;
  }
  .contact-strip__brand {
    display: flex; align-items: center; gap: 10px;
    font-weight: 800; letter-spacing: .3px;
  }
  .contact-strip__mark { width: 12px; height: 12px; background: var(--teal); }
  .contact-strip__web { font-weight: 500; letter-spacing: .5px; }
</style>
</head>
<body>

<section class="card card--front">
  <div class="cover-photo" role="img" aria-label="Close-up photo of a CNC lathe turret and spindle, toned orange on the left and teal on the right"></div>
  <div class="brand-tab">
    <span class="brand-tab__mark"></span>
    <span class="brand-tab__name">Kelvra Controls</span>
  </div>
  <h1 class="tagline">PIONEERING<br><strong>RESPONSIVE</strong><br>MACHINING</h1>
  <div class="service-label">
    <span class="service-label__text">MACHINING</span>
    <span class="service-label__bar"></span>
  </div>
</section>

<section class="card card--back">
  <div class="back-photo" role="img" aria-label="Dark faded photo of CNC machinery in the background"></div>
  <h2 class="heading">COMPUTER<br>NUMERIC<br>CONTROL (CNC)</h2>
  <p class="intro">CNC machining offers the most efficient method of producing steel and plastic components. The CNC is programmed using computer code to generate a digital machining process that can be repeated and precisely controlled. Repetitive tasks such as drilling, threading, and tapping are made simple using this technology.</p>

  <svg width="0" height="0" style="position:absolute">
    <defs>
      <symbol id="tick" viewBox="0 0 20 20">
        <circle cx="10" cy="10" r="10" fill="#1a8f8f"/>
        <path d="M5.5 10.3l3 3 6-6.3" fill="none" stroke="#fff" stroke-width="2.2" stroke-linecap="round" stroke-linejoin="round"/>
      </symbol>
    </defs>
  </svg>

  <ul class="capabilities capabilities--left">
    <li><svg><use href="#tick"/></svg>Lathe &amp; Turning Centers up to 36" Dia.</li>
    <li><svg><use href="#tick"/></svg>Mill &amp; Machining Centers up to 120" L</li>
    <li><svg><use href="#tick"/></svg>Complex Multi-Axis Machining up to 8-Axis</li>
    <li><svg><use href="#tick"/></svg>Swiss Screw Machining</li>
    <li><svg><use href="#tick"/></svg>Deep Hole Drilling/Trepanning</li>
    <li><svg><use href="#tick"/></svg>CNC Honing &amp; Grinding</li>
  </ul>
  <ul class="capabilities capabilities--right">
    <li><svg><use href="#tick"/></svg>CNC Laser &amp; Cladding</li>
    <li><svg><use href="#tick"/></svg>CNC Press</li>
    <li><svg><use href="#tick"/></svg>CNC Plasma &amp; Water Jet</li>
    <li><svg><use href="#tick"/></svg>Oil Field and Custom Threading</li>
    <li><svg><use href="#tick"/></svg>3D Surfacing and Mold Machining</li>
    <li><svg><use href="#tick"/></svg>Large Capacity Band Saw Cutting</li>
  </ul>

  <div class="info-band">
    <ul class="highlights">
      <li>
        <svg viewBox="0 0 22 22"><path d="M3 5h16M11 5v14M7 19h8" fill="none" stroke="#fff" stroke-width="2.4" stroke-linecap="round"/></svg>
        SWISS SCREW &amp; SMALL PARTS
      </li>
      <li>
        <svg viewBox="0 0 22 22"><circle cx="11" cy="11" r="6" fill="none" stroke="#fff" stroke-width="2.4"/><circle cx="11" cy="11" r="2" fill="#fff"/><path d="M11 1v3M11 18v3M1 11h3M18 11h3M4 4l2 2M16 16l2 2M4 18l2-2M16 6l2-2" stroke="#fff" stroke-width="2.2" stroke-linecap="round"/></svg>
        AUTOMATION
      </li>
      <li>
        <svg viewBox="0 0 22 22"><circle cx="11" cy="12" r="8" fill="none" stroke="#fff" stroke-width="2.4"/><path d="M11 8v4l3 2M4 3l-2 2M18 3l2 2" fill="none" stroke="#fff" stroke-width="2.2" stroke-linecap="round"/></svg>
        24HR SERVICE, REPAIR AND WELDING
      </li>
    </ul>
    <div class="gallery">
      <figure class="gallery__item">
        <div class="gallery__photo" role="img" aria-label="Photo of a lathe turning a metal part"></div>
        <figcaption class="gallery__label">LATHE / TURNING</figcaption>
      </figure>
      <figure class="gallery__item">
        <div class="gallery__photo" role="img" aria-label="Photo of a milling cutter on a workpiece"></div>
        <figcaption class="gallery__label">MILLING</figcaption>
      </figure>
      <figure class="gallery__item">
        <div class="gallery__photo" role="img" aria-label="Photo of a Swiss screw machine"></div>
        <figcaption class="gallery__label">SWISS</figcaption>
      </figure>
      <figure class="gallery__item">
        <div class="gallery__photo" role="img" aria-label="Photo of a 5-axis machining head"></div>
        <figcaption class="gallery__label">5-AXIS</figcaption>
      </figure>
    </div>
  </div>

  <footer class="contact-strip">
    <span class="contact-strip__brand"><span class="contact-strip__mark"></span>Kelvra Controls</span>
    <span class="contact-strip__web">www.kelvracontrols.ca</span>
  </footer>
</section>

</body>
</html>
```